Allergy Social Media Advertising Graphics Needed

We already have the copy written for KT and Vistaloop ads and need a designer to ad a graphic element to the campaign.

Target Market(s)

Mostly soccer moms, suburban Washington, DC, highly educated, smart and research oriented.

Font styles to use
Sans Serif

Requirements
Must have
• An eye-catching concept that makes people stop scrolling and pay attention to the advertisement.
Nice to have
• Clean and simple design. Bold approach with an elegant feel.
Should not have
• Too busy or cartoon-like designs.

```html
<!DOCTYPE html>
<html lang="en">
<head>
<meta charset="utf-8">
<title>Peanut Allergy Oral Immunotherapy Ads</title>
<link rel="stylesheet" href="https://fonts.googleapis.com/css2?family=Montserrat:ital,wght@0,500;1,800;1,900&display=swap">
<style>
  :root {
    --board-light: #a9c58a;
    --board-mid: #4f7f5c;
    --board-dark: #13233f;
    --ad-orange: #f2a15f;
    --ad-orange-deep: #e0813d;
    --ad-glow: #fff1cf;
    --ink-dark-red: #a11d12;
    --ink-red: #d8061a;
    --ink-white: #fffaf2;
    --button-red: #c9000f;
    --cream: #f7ead5;
    --peanut-shell: #e6c79a;
    --peanut-skin: #b8503e;
  }
  * { margin: 0; padding: 0; box-sizing: border-box; }
  html, body { width: 1200px; height: 1200px; overflow: hidden; }
  body {
    position: relative;
    font-family: "Montserrat", Arial, sans-serif;
    background:
      radial-gradient(ellipse 55% 60% at 50% 48%, var(--board-light) 0%, #7fa772 35%, var(--board-mid) 70%, var(--board-dark) 120%);
  }
  .ad {
    position: absolute;
    overflow: hidden;
    background:
      radial-gradient(ellipse 60% 70% at 92% 20%, var(--ad-glow) 0%, rgba(255,230,180,0.6) 25%, transparent 60%),
      linear-gradient(135deg, var(--ad-orange) 0%, #f6b06f 55%, var(--ad-orange-deep) 100%);
  }
  .ad-banner { left: 275px; top: 195px; width: 652px; height: 340px; }
  .ad-square {
    left: 407px; top: 629px; width: 388px; height: 387px;
    background:
      radial-gradient(ellipse 70% 55% at 0% 30%, var(--ad-glow) 0%, rgba(255,230,180,0.55) 30%, transparent 65%),
      linear-gradient(160deg, var(--ad-orange-deep) 0%, var(--ad-orange) 45%, #f5ad6c 100%);
  }
  .headline {
    position: absolute;
    font-weight: 900;
    font-style: italic;
    color: var(--ink-dark-red);
    letter-spacing: -0.5px;
  }
  .headline .accent { color: var(--ink-red); }
  .subhead {
    position: absolute;
    font-weight: 900;
    font-style: italic;
    color: var(--ink-white);
    letter-spacing: -0.5px;
    text-shadow: 1px 2px 3px rgba(140, 60, 20, 0.35);
  }
  .cta {
    position: absolute;
    background: var(--button-red);
    color: #fff;
    border-radius: 3px;
    font-weight: 500;
    text-align: center;
  }
  .ad-banner .headline { left: 45px; top: 58px; font-size: 27px; line-height: 26px; }
  .ad-banner .subhead { left: 45px; top: 160px; font-size: 36px; line-height: 33px; }
  .ad-banner .cta { left: 45px; top: 265px; width: 189px; height: 31px; font-size: 17px; line-height: 31px; }
  .ad-banner .peanut-art {
    position: absolute; left: 340px; top: 0; width: 312px; height: 340px;
    background:
      radial-gradient(ellipse 22% 12% at 42% 22%, var(--peanut-shell) 0%, transparent 100%),
      radial-gradient(ellipse 30% 16% at 80% 58%, var(--peanut-skin) 0%, transparent 100%),
      radial-gradient(ellipse 22% 11% at 35% 82%, var(--peanut-shell) 0%, transparent 100%);
  }
  .ad-square .headline { left: 0; width: 388px; text-align: center; top: 67px; font-size: 26px; line-height: 27.5px; }
  .ad-square .subhead { left: 0; width: 388px; text-align: center; top: 202px; font-size: 23px; line-height: 23px; }
  .ad-square .cta { left: 131px; top: 281px; width: 126px; height: 21px; font-size: 11px; line-height: 21px; }
  .ad-square .peanut-art {
    position: absolute; left: 0; top: 0; width: 388px; height: 387px;
    background:
      radial-gradient(ellipse 11% 8% at 10% 14%, var(--peanut-shell) 0%, transparent 100%),
      radial-gradient(ellipse 8% 7% at 5% 55%, var(--peanut-shell) 0%, transparent 100%),
      radial-gradient(ellipse 18% 9% at 17% 78%, var(--peanut-skin) 0%, transparent 100%),
      radial-gradient(ellipse 12% 6% at 46% 89%, var(--peanut-shell) 0%, transparent 100%);
  }
  .torn-edge { position: absolute; left: 0; bottom: 0; width: 100%; display: block; }
  .ad-banner .torn-edge { height: 14px; }
  .ad-square .torn-edge { height: 62px; }
</style>
</head>
<body>
  <section class="ad ad-banner">
    <div class="peanut-art" role="img" aria-label="Shelled and split peanuts flying in warm light rays"></div>
    <svg class="torn-edge" viewBox="0 0 652 14" preserveAspectRatio="none" aria-hidden="true">
      <polygon points="600,14 608,8 616,11 626,4 636,9 646,3 652,5 652,14" fill="var(--cream)"/>
    </svg>
    <h1 class="headline">Is worrying about your<br>child’s <span class="accent">Peanut Allergy</span><br>driving you nuts?</h1>
    <p class="subhead">Oral Immunotherapy<br>Could Help.</p>
    <a class="cta">Learn more</a>
  </section>

  <section class="ad ad-square">
    <svg class="torn-edge" viewBox="0 0 388 62" preserveAspectRatio="none" aria-hidden="true">
      <polygon points="0,10 20,6 40,12 62,4 88,9 110,3 136,11 160,8 190,14 220,10 250,15 280,13 300,17 318,12 336,18 352,14 370,19 388,16 388,62 0,62" fill="var(--cream)"/>
    </svg>
    <div class="peanut-art" role="img" aria-label="Peanuts in the shell and split peanut halves scattered around the frame"></div>
    <h2 class="headline">Is worrying about<br>your child’s<br><span class="accent">Peanut Allergy</span><br>driving you nuts?</h2>
    <p class="subhead">Oral Immunotherapy<br>Could Help.</p>
    <a class="cta">Learn more</a>
  </section>
</body>
</html>
```